Maple Lantern Business Card

Design of business cards

Target Market(s)

We are aiming as small business owners who need anything from basic business structures, website plans, business processes and quality assurance.

Industry/Entity Type

Business

Colors

Designer to choose colors to be used in the design.

Requirements
Nice to have
• I would prefer one side of the card to use the green from the logo. Prefer to have the same font as the logo.

```html
<!DOCTYPE html>
<html lang="en">
<head>
<meta charset="utf-8">
<title>Maple Lantern Consulting – Business Card</title>
<link rel="stylesheet" href="https://fonts.googleapis.com/css2?family=Cinzel:wght@500&display=swap">
<style>
  :root {
    --backdrop: #d6d6d6;
    --card-black: #231f20;
    --brand-green: #9bca3c;
    --rule-grey: #bdbdbd;
    --label-white: #f2f2f2;
  }
  * { margin: 0; padding: 0; box-sizing: border-box; }
  html, body {
    width: 1200px;
    height: 1200px;
    overflow: hidden;
    background: var(--backdrop);
  }
  .card {
    position: absolute;
    left: 230px;
    top: 383px;
    width: 740px;
    height: 434px;
    background: var(--card-black);
    font-family: "Cinzel", serif;
  }
  .brand {
    position: absolute;
    left: 69px;
    top: 75px;
    display: flex;
    align-items: center;
    gap: 20px;
  }
  .brand-mark {
    width: 76px;
    height: 76px;
    background: var(--brand-green);
  }
  .brand-name {
    color: var(--brand-green);
    font-weight: 500;
    font-size: 22px;
    line-height: 26px;
    letter-spacing: 0.5px;
  }
  .signature-rule {
    position: absolute;
    left: 65px;
    top: 333px;
    width: 362px;
    height: 1px;
    background: var(--rule-grey);
  }
  .contact-labels {
    position: absolute;
    left: 443px;
    top: 325px;
    list-style: none;
    color: var(--label-white);
    font-size: 14px;
    line-height: 26px;
    letter-spacing: 1px;
  }
</style>
</head>
<body>
  <section class="card">
    <div class="brand">
      <div class="brand-mark"></div>
      <p class="brand-name">Maple<br>Lantern<br>Consulting</p>
    </div>
    <div class="signature-rule"></div>
    <ul class="contact-labels">
      <li>NAME-</li>
      <li>PHONE-</li>
    </ul>
  </section>
</body>
</html>
```